Maple Ridge business card design

Card needs to include the following text/items:
Company Logo
Tobin Marsh
Phone # - 555-318-7642
service@mapleridgelandscaping.example
Lawn & landscape maintenance services

```html
<!DOCTYPE html>
<html lang="en">
<head>
<meta charset="utf-8">
<title>Maple Ridge Landscaping – Business Card</title>
<link rel="stylesheet" href="https://fonts.googleapis.com/css2?family=Cinzel:wght@400;700&family=Cormorant+Garamond:wght@500&family=Crimson+Text:ital@0;1&display=swap">
<style>
  :root {
    --page-bg: #d9d4cc;
    --panel-dark: #0f2419;
    --panel-mid: #2a4a3b;
    --accent-green: #4f6a2a;
    --ring-green: #3d5a1e;
    --text-light: #ece8dd;
    --logo-ink: #14261a;
    --scene-sky: #c9d3d6;
    --scene-ground: #b7ae94;
  }
  * { margin: 0; padding: 0; box-sizing: border-box; }
  html, body {
    width: 1200px; height: 969px; overflow: hidden;
    background: var(--page-bg);
  }
  .card {
    position: absolute; left: 100px; top: 200px;
    width: 1000px; height: 568px;
    border-radius: 26px; overflow: hidden;
    box-shadow: 0 18px 40px rgba(0,0,0,.25);
  }
  .card-art { position: absolute; inset: 0; }
  .accent-bar {
    position: absolute; left: 0; top: 78px;
    width: 12px; height: 150px; background: var(--accent-green);
  }
  .holder-name {
    position: absolute; left: 65px; top: 66px;
    font: 400 41px/1 "Cinzel", serif; color: var(--text-light);
    letter-spacing: 1px;
  }
  .contact { position: absolute; left: 65px; top: 128px; color: var(--text-light); }
  .contact-row { display: flex; align-items: center; gap: 12px; }
  .contact-row svg { flex: none; fill: var(--text-light); }
  .phone { font: 500 40px/1 "Cormorant Garamond", serif; margin-bottom: 10px; }
  .email { font: italic 400 20px/1 "Crimson Text", serif; margin-bottom: 8px; }
  .web { font: 400 21px/1 "Crimson Text", serif; }
  .services {
    position: absolute; left: 65px; top: 335px;
    font: 400 32px/38px "Cinzel", serif; color: var(--text-light);
    letter-spacing: 1px;
  }
  .brand {
    position: absolute; left: 545px; top: 180px; width: 400px;
    text-align: center;
  }
  .brand-dot {
    width: 220px; height: 220px; border-radius: 50%;
    background: var(--logo-ink); margin: 0 auto 22px;
  }
  .brand-name {
    font: 700 52px/1 "Cinzel", serif; color: var(--logo-ink);
  }
</style>
</head>
<body>
  <div class="card">
    <svg class="card-art" width="1000" height="568" viewBox="0 0 1000 568">
      <defs>
        <radialGradient id="panelGrad" cx="0.3" cy="0.6" r="0.8">
          <stop offset="0" stop-color="#2f5142"/>
          <stop offset="1" stop-color="#0e2218"/>
        </radialGradient>
        <linearGradient id="sceneGrad" x1="0" y1="0" x2="0" y2="1">
          <stop offset="0" stop-color="#c3cfd4"/>
          <stop offset="0.55" stop-color="#cfcabb"/>
          <stop offset="1" stop-color="#b2a98d"/>
        </linearGradient>
      </defs>
      <rect width="1000" height="568" fill="url(#panelGrad)"/>
      <g role="img" aria-label="Soft landscape scene with bare tree, evergreen, hills, fence and setting sun">
        <circle cx="770" cy="330" r="360" fill="url(#sceneGrad)"/>
      </g>
      <circle cx="770" cy="330" r="372" fill="none" stroke="#dcdcd6" stroke-width="10"/>
      <circle cx="770" cy="330" r="380" fill="none" stroke="var(--ring-green)" stroke-width="6"/>
      <circle cx="770" cy="330" r="340" fill="none" stroke="#9aa57c" stroke-width="3" opacity=".6"/>
    </svg>

    <div class="accent-bar"></div>
    <h1 class="holder-name">TOBIN MARSH</h1>

    <div class="contact">
      <div class="contact-row phone">
        <svg width="22" height="22" viewBox="0 0 24 24"><path d="M6.6 10.8a15 15 0 0 0 6.6 6.6l2.2-2.2c.3-.3.7-.4 1-.2 1.1.4 2.3.6 3.6.6.6 0 1 .4 1 1V20c0 .6-.4 1-1 1A17 17 0 0 1 3 4c0-.6.4-1 1-1h3.5c.6 0 1 .4 1 1 0 1.3.2 2.5.6 3.6.1.3 0 .7-.2 1z"/></svg>
        <span>555-318-7642</span>
      </div>
      <div class="contact-row email">
        <svg width="22" height="16" viewBox="0 0 22 16"><path d="M0 0h22v16H0zM2 2v1l9 6 9-6V2L11 8z"/></svg>
        <span>service@mapleridgelandscaping.example</span>
      </div>
      <div class="contact-row web">
        <svg width="22" height="22" viewBox="0 0 24 24"><circle cx="12" cy="12" r="10"/></svg>
        <span>mapleridgelandscaping.example</span>
      </div>
    </div>

    <p class="services">LAWN &amp;<br>LANDSCAPE<br>MAINTENANCE<br>SERVICES</p>

    <div class="brand">
      <div class="brand-dot"></div>
      <div class="brand-name">MAPLE RIDGE</div>
    </div>
  </div>
</body>
</html>
```